Corvantine Services

Double sided business cards with color on front and black and white on back. I have basic ideas and graphics, but am looking for someone to take them to the next level

```html
<!DOCTYPE html>
<html lang="en">
<head>
<meta charset="utf-8">
<title>Corvantine Services – Business Card, Front and Back</title>
<link rel="stylesheet" href="https://fonts.googleapis.com/css2?family=Barlow+Condensed:wght@400;500&display=swap">
<style>
  :root {
    --backdrop: #2a2a2a;
    --brand-blue: #4a8db5;
    --paper: #f7f7f7;
    --accent-red: #d8362e;
    --accent-yellow: #e8d23a;
    --ink: #111111;
    --black: #050505;
    --white: #ffffff;
  }
  html, body {
    margin: 0;
    padding: 0;
    width: 1200px;
    height: 732px;
    overflow: hidden;
    background: var(--backdrop);
    font-family: "Barlow Condensed", "Arial Narrow", sans-serif;
  }
  .canvas {
    position: relative;
    width: 1200px;
    height: 732px;
  }
  .card {
    position: absolute;
    top: 242px;
    width: 436px;
    height: 248px;
    overflow: hidden;
  }
  .card--front { left: 144px; background: var(--brand-blue); }
  .card--back  { left: 621px; background: var(--black); }
  .card__shapes {
    position: absolute;
    inset: 0;
    width: 100%;
    height: 100%;
  }
  .brand-mark {
    position: absolute;
    display: flex;
    align-items: center;
    gap: 8px;
    font-weight: 500;
    font-size: 22px;
    letter-spacing: 0.4px;
    line-height: 1;
    white-space: nowrap;
  }
  .brand-mark__dot {
    width: 40px;
    height: 40px;
    border-radius: 50%;
    flex: none;
  }
  .card--front .brand-mark { left: 272px; top: 66px; color: var(--brand-blue); }
  .card--front .brand-mark__dot { background: var(--brand-blue); }
  .card--back .brand-mark { left: 15px; top: 66px; color: var(--ink); }
  .card--back .brand-mark__dot { background: var(--ink); }

  .company-name,
  .company-phone {
    position: absolute;
    right: 23px;
    margin: 0;
    font-size: 26px;
    line-height: 1;
    text-transform: uppercase;
    white-space: nowrap;
  }
  .company-name { top: 166px; color: var(--brand-blue); font-weight: 500; }
  .company-phone { top: 191px; color: var(--ink); font-weight: 400; }

  .tagline {
    position: absolute;
    left: 15px;
    top: 166px;
    margin: 0;
    font-size: 24px;
    font-weight: 400;
    line-height: 24.5px;
    color: var(--ink);
    text-transform: uppercase;
    white-space: nowrap;
  }
</style>
</head>
<body>
<main class="canvas">

  <section class="card card--front" aria-label="Business card front">
    <svg class="card__shapes" viewBox="0 0 895 510" preserveAspectRatio="none" aria-hidden="true">
      <defs>
        <linearGradient id="front-shard" x1="0" y1="0" x2="1" y2="0">
          <stop offset="0" stop-color="#dcdcdc"/>
          <stop offset="1" stop-color="#f7f7f7" stop-opacity="0"/>
        </linearGradient>
      </defs>
      <polygon points="645,0 895,0 895,429 853,470 175,470" fill="var(--paper)"/>
      <polygon points="245,470 480,230 400,470" fill="url(#front-shard)" opacity="0.7"/>
      <polygon points="340,470 500,310 420,470" fill="url(#front-shard)" opacity="0.6"/>
      <line x1="617" y1="0" x2="283" y2="334" stroke="var(--accent-red)" stroke-width="2"/>
      <line x1="155" y1="490" x2="598" y2="490" stroke="var(--white)" stroke-width="2"/>
      <line x1="870" y1="484" x2="893" y2="462" stroke="var(--accent-yellow)" stroke-width="2"/>
    </svg>
    <div class="brand-mark"><span class="brand-mark__dot"></span>CORVANTINE</div>
    <h1 class="company-name">Corvantine Services</h1>
    <p class="company-phone">555-014-2290</p>
  </section>

  <section class="card card--back" aria-label="Business card back">
    <svg class="card__shapes" viewBox="0 0 895 510" preserveAspectRatio="none" aria-hidden="true">
      <defs>
        <linearGradient id="back-shard" x1="0" y1="0" x2="1" y2="0">
          <stop offset="0" stop-color="#f7f7f7" stop-opacity="0"/>
          <stop offset="1" stop-color="#d6d6d6"/>
        </linearGradient>
      </defs>
      <polygon points="0,0 250,0 718,470 43,470 0,428" fill="var(--paper)"/>
      <polygon points="410,230 640,470 560,470" fill="url(#back-shard)" opacity="0.7"/>
      <polygon points="400,310 560,470 480,470" fill="url(#back-shard)" opacity="0.6"/>
      <line x1="275" y1="0" x2="610" y2="334" stroke="var(--white)" stroke-width="2"/>
      <line x1="297" y1="490" x2="739" y2="490" stroke="var(--white)" stroke-width="2"/>
      <line x1="0" y1="442" x2="25" y2="482" stroke="var(--white)" stroke-width="2"/>
    </svg>
    <div class="brand-mark"><span class="brand-mark__dot"></span>CORVANTINE</div>
    <p class="tagline">A Curated Experience<br>All That Is Promised Is Clarity</p>
  </section>

</main>
</body>
</html>
```